Landing page for a cyber security service provider called 'Lumen Grove'

The client is a new cyber security company in need of a website landing page at lumengrove.example.

Their visual identity is modern, playful, clean and uncluttered and represents innovation, connectivity and approachability.

The company logo is provided in black (attached) but the client is open to changing the colour to align with the new website design.

The landing page needs to contain:
- A call to action with a 'Get Started' button
-Links to blank 'How it works', 'Products', 'Pricing', 'About Us' and 'Contact Us' pages (that we'll fill out later)

Target Market(s)

Medium to large businesses who probably don't understand cyber / cyber security but need their business to be protected.

Industry/Entity Type

Cyber Security

Coding

Coded - Design and coding required

Number of Pages Required

1 page

Font styles to use
Sans Serif
Other font styles liked:
• Helvetica

Requirements
Nice to have
• Hero banner at the top of the landing page.
Should not have
• Should not look like a traditional cyber / cyber security design (eg no dark blue/ black, red/black colour combinations). Please no military styles (eg no shields, cannons, swords, guns)

```html
<!DOCTYPE html>
<html lang="en">
<head>
<meta charset="utf-8">
<title>Lumen Grove – Cyber Security Solutions</title>
<link href="https://fonts.googleapis.com/css2?family=Open+Sans:wght@400;500;600;700&display=swap" rel="stylesheet">
<style>
:root{
  --brand:#2a6fd6;
  --brand-deep:#1d5bb8;
  --blue:#1585e6;
  --sky:#4fa3f0;
  --ink:#1d1d2b;
  --muted:#767a8e;
  --light:#f3f5f9;
  --footer:#1e5bb8;
  --footer-soft:#2c6ac6;
  --footer-text:#dce8fa;
  --hero-a:#2f6fd0;
  --hero-b:#5aa0ea;
  --orange:#ff5a1f;
}
*{margin:0;padding:0;box-sizing:border-box}
html,body{width:1200px;height:4240px;overflow:hidden}
body{font-family:"Open Sans",Helvetica,Arial,sans-serif;color:var(--ink);background:#fff;position:relative}
a{text-decoration:none;color:inherit}
.abs{position:absolute}

/* header */
.topbar{left:400px;top:0;width:800px;height:36px;background:var(--brand);color:#eaf2fd;font-size:11px}
.topbar span{position:absolute;top:11px;white-space:nowrap}
.topbar .dot{display:inline-block;width:7px;height:7px;background:#eaf2fd;margin-left:6px;vertical-align:middle}
.quote{position:absolute;left:440px;top:0;height:28px;width:105px;color:#fff;font-size:10px;text-align:center;line-height:38px;border-bottom:3px solid #3bb06a}
.logo{left:106px;top:46px;display:flex;align-items:center;gap:8px;font-weight:700;font-size:16px;color:var(--ink)}
.logo i{width:14px;height:14px;border-radius:50%;background:var(--blue);display:block}
.nav{top:52px;left:447px;font-size:11px;color:#5d6274}
.nav a{position:absolute;white-space:nowrap}
.nav a.on{color:var(--blue);font-weight:600}

/* hero */
.hero{left:0;top:82px;width:1200px;height:718px;background:linear-gradient(100deg,var(--hero-a) 0%,#4386dc 55%,var(--hero-b) 100%);overflow:hidden}
.hero-people{left:708px;top:148px;width:492px;height:570px;background:linear-gradient(180deg,#b6cdee,#7fa6dc)}
.welcome{left:105px;top:190px;color:#fff;font-size:20px;letter-spacing:.5px}
.hero h1{position:absolute;left:105px;top:208px;color:#fff;font-size:50px;line-height:60px;font-weight:700;width:640px}
.hero p{position:absolute;left:105px;top:338px;color:#eef4fd;font-size:16px;line-height:30px;width:500px}
.btn{position:absolute;background:var(--blue);color:#fff;font-weight:600;font-size:16px;display:flex;align-items:center;gap:18px;padding:0 20px;height:45px}
.hero .btn{background:#fff;color:var(--brand)}

/* about */
.ring{left:105px;top:845px;width:468px;height:468px;border-radius:50%;border:6px solid var(--brand);border-left-color:transparent;transform:rotate(-20deg)}
.about-photo{left:115px;top:870px;width:445px;height:445px;border-radius:50%;background:linear-gradient(135deg,#7a6a5a,#c3b6a8 60%,#e2dcd5)}
.eyebrow{font-size:13px;color:var(--blue);padding-bottom:6px;border-bottom:2px solid var(--blue);position:absolute;white-space:nowrap}
.h2{position:absolute;color:var(--brand);font-weight:700}
.body{position:absolute;color:var(--muted);font-size:13px;line-height:22px}

/* services */
.svc-band{left:0;top:1399px;width:1200px;height:413px;background:linear-gradient(100deg,#2f6fd0,#4a8fe0 50%,#3478d6)}
.card{position:absolute;top:1600px;width:324px;height:355px;background:#fff;box-shadow:0 2px 10px rgba(0,0,0,.1)}
.card .img{position:absolute;left:19px;top:18px;width:288px;height:194px}
.card .ic{position:absolute;left:19px;top:162px;width:50px;height:50px;background:var(--blue);display:flex;align-items:center;justify-content:center}
.card h3{position:absolute;left:17px;top:241px;font-size:19px;font-weight:600;color:var(--ink)}
.card p{position:absolute;left:17px;top:283px;font-size:13px;line-height:22px;color:var(--muted);width:280px}

/* why */
.why-bg{left:0;top:1955px;width:1200px;height:703px;background:var(--light)}
.why-halo{left:403px;top:2156px;width:396px;height:396px;border-radius:50%;background:#e8eef8}
.why-ring{left:440px;top:2193px;width:322px;height:322px;border-radius:50%;background:#d4e2f6}
.why-photo{left:454px;top:2207px;width:294px;height:294px;border-radius:50%;background:linear-gradient(180deg,#c8cdd6,#7b8594)}
.feat{position:absolute;background:#fff;border-radius:10px;box-shadow:0 2px 8px rgba(0,0,0,.06);height:105px}
.feat h4{position:absolute;top:16px;font-size:20px;font-weight:500;color:var(--ink);white-space:nowrap}
.feat p{position:absolute;top:50px;font-size:12.5px;line-height:21px;color:var(--muted);width:190px}
.bub{position:absolute;width:66px;height:66px;border-radius:50%;background:#fff;box-shadow:0 2px 8px rgba(0,0,0,.08);display:flex;align-items:center;justify-content:center}

/* contact */
.contact-band{left:0;top:2658px;width:1200px;height:466px;background:linear-gradient(100deg,#2f6fd0,#4c92e3 55%,#3477d4)}
.contact-band h2{position:absolute;left:130px;top:58px;color:#fff;font-size:42px;font-weight:700}
.contact-band .sub{position:absolute;left:132px;top:118px;color:#eef4fd;font-size:14px}
.citem{position:absolute;left:130px;display:flex;gap:16px;color:#fff}
.citem .cc{width:46px;height:46px;border-radius:50%;background:#fff;display:flex;align-items:center;justify-content:center;flex:none}
.citem small{display:block;font-size:14px;color:#eef4fd}
.citem b{display:block;font-size:19px;line-height:24px;font-weight:700}
.form{left:678px;top:2788px;width:390px;height:367px;background:var(--blue)}
.field{position:absolute;left:22px;width:345px;height:38px;background:#fff;border:1px solid #d2d6e0;font-size:10px;color:#8b8fa0;padding:12px 14px}
.submit{position:absolute;left:22px;top:295px;width:345px;height:38px;background:var(--brand-deep);color:#fff;font-size:12px;font-weight:700;text-align:center;line-height:38px}

/* testimonials */
.tcard{position:absolute;top:3353px;width:497px;height:257px;background:var(--light)}
.tcard .bar{position:absolute;left:62px;top:20px;width:2px;height:210px;background:var(--brand)}
.tcard .q{position:absolute;left:40px;top:100px;width:46px;height:46px;border-radius:50%;background:var(--brand);border:4px solid #fff;box-shadow:0 0 0 2px var(--brand)}
.tcard .stars{position:absolute;left:116px;top:46px;color:var(--orange);font-size:14px;letter-spacing:4px}
.tcard p{position:absolute;left:116px;top:86px;width:345px;font-size:14px;line-height:22px;color:var(--muted)}
.tcard h5{position:absolute;left:116px;top:180px;font-size:17px;font-weight:700;color:var(--ink)}
.tcard span.loc{position:absolute;left:116px;top:207px;font-size:12.5px;color:var(--muted)}
.tcard .av{position:absolute;right:40px;top:170px;width:56px;height:56px;border-radius:50%;background:linear-gradient(135deg,#c9ccd3,#7c8290)}
.dots{left:566px;top:3652px;display:flex;gap:8px}
.dots i{width:10px;height:10px;border-radius:50%;background:#d8d8de;display:block}
.dots i.on{background:#fff;border:2px solid var(--orange)}

/* footer */
.footer{left:0;top:3700px;width:1200px;height:540px;background:var(--footer);color:var(--footer-text)}
.footer h6{position:absolute;color:#fff;font-size:14px;font-weight:700;top:128px}
.flinks{position:absolute;top:172px;font-size:12.5px;line-height:26px}
.soc{position:absolute;top:275px;width:30px;height:30px;background:var(--footer-soft)}
.soc.on{background:var(--sky)}
.news{position:absolute;left:826px;top:218px;width:195px;height:47px;background:#fff;color:#8b8fa0;font-size:11px;padding:16px 24px}
.news-btn{position:absolute;left:1021px;top:218px;width:50px;height:47px;background:var(--sky);display:flex;align-items:center;justify-content:center}
.finfo{position:absolute;top:370px;display:flex;gap:16px;align-items:center}
.finfo .fc{width:46px;height:46px;border-radius:50%;background:var(--footer-soft);display:flex;align-items:center;justify-content:center}
.finfo .fc.on{background:var(--sky)}
.finfo b{display:block;color:#fff;font-size:14.5px}
.finfo small{display:block;font-size:11.5px}
</style>
</head>
<body>

<!-- Header -->
<header>
  <div class="abs topbar">
    <svg class="abs" style="left:63px;top:12px" width="9" height="12" viewBox="0 0 9 12"><path d="M4.5 0a4.5 4.5 0 0 0-4.5 4.5C0 8 4.5 12 4.5 12S9 8 9 4.5A4.5 4.5 0 0 0 4.5 0z" fill="#eaf2fd"/></svg>
    <span style="left:80px">48 Orchard Lane, Brookfield 20415</span>
    <span style="left:305px">Follow Us: <i class="dot"></i><i class="dot"></i><i class="dot"></i></span>
    <div class="quote">GET QUOTATION</div>
  </div>
  <svg class="abs" style="left:0;top:0" width="440" height="36" viewBox="0 0 440 36"><path d="M0 0H400C418 0 425 36 440 36H0Z" fill="#fff"/></svg>
  <div class="abs logo"><i></i>Lumen Grove</div>
  <nav class="abs nav">
    <a class="on" href="#" style="left:0">Home</a>
    <a href="#" style="left:94px">How it works</a>
    <a href="#" style="left:210px">Products</a>
    <a href="#" style="left:310px">Pricing</a>
    <a href="#" style="left:405px">About Us</a>
    <a href="#" style="left:520px">Contact Us</a>
  </nav>
</header>

<!-- Hero -->
<section class="abs hero">
  <div class="abs hero-people" role="img" aria-label="Two colleagues reviewing a tablet together"></div>
  <div class="abs welcome">WELCOME</div>
  <h1>Cyber security Solutions Tailored for You</h1>
  <p>Lorem ipsum dolor sit amet, consectetur adipiscing elit, sed do eiusmod tempor incididunt ut labore et dolore magna aliqua.</p>
  <a class="btn" href="#" style="left:107px;top:476px">Get Started
    <svg width="18" height="14" viewBox="0 0 18 14"><path d="M0 7h16M10 1l6 6-6 6" fill="none" stroke="currentColor" stroke-width="1.8"/></svg></a>
</section>
<svg class="abs" style="left:0;top:690px" width="1200" height="130" viewBox="0 0 1200 130">
  <path d="M0 66C200 40 400 40 600 70S1000 100 1200 30V130H0Z" fill="var(--blue)"/>
  <path d="M0 66C200 40 400 40 600 78S1000 90 1200 70V130H0Z" fill="#fff"/>
</svg>

<!-- Who we are -->
<section>
  <div class="abs ring"></div>
  <div class="abs about-photo" role="img" aria-label="Two team members working together at a desk"></div>
  <div class="eyebrow" style="left:613px;top:861px">WHO WE ARE</div>
  <h2 class="h2" style="left:612px;top:898px;font-size:42px;line-height:50px">Mitigating Risks,<br>Ensuring Safety</h2>
  <div class="abs" style="left:612px;top:1029px;font-size:21px;color:#2b2d3c">Your Partner in Safety and Compliance</div>
  <p class="body" style="left:613px;top:1072px;width:510px">Lorem ipsum dolor sit amet, consectetur adipiscing elit, sed do eiusmod temp or incididunt ut labore et dolore magna aliqua. Ut enim ad minim veniam, quis laboris nisi ut aliquip ex ea commodo consequat.</p>
  <p class="body" style="left:613px;top:1148px;width:510px">Lorem ipsum dolor sit amet, consectetur adipiscing elit, sed do eiusmod temp or incididunt ut labore et dolore magna aliqua.</p>
  <a class="btn" href="#" style="left:612px;top:1231px">Contact us
    <svg width="18" height="14" viewBox="0 0 18 14"><path d="M0 7h16M10 1l6 6-6 6" fill="none" stroke="#fff" stroke-width="1.8"/></svg></a>
</section>

<!-- Services -->
<section>
  <div class="abs svc-band" role="img" aria-label="Blurred office team in the background"></div>
  <div class="abs" style="left:85px;top:1462px;color:#fff;font-size:13px;padding-bottom:6px;border-bottom:2px solid #fff">SERVICES</div>
  <h2 class="abs" style="left:84px;top:1494px;color:#fff;font-size:42px;font-weight:700">Services We Provide</h2>
  <div class="abs" style="left:930px;top:1512px;color:#fff;font-size:15px">More Services</div>
  <div class="abs" style="left:1073px;top:1503px;width:40px;height:39px;background:#fff;display:flex;align-items:center;justify-content:center">
    <svg width="10" height="14" viewBox="0 0 10 14"><path d="M2 1l6 6-6 6" fill="none" stroke="var(--blue)" stroke-width="2"/></svg></div>

  <div class="card" style="left:86px">
    <div class="img" role="img" aria-label="Business partners discussing over a tablet" style="background:linear-gradient(135deg,#6d7d95,#c7ced8)"></div>
    <div class="ic"><svg width="24" height="24" viewBox="0 0 24 24"><path d="M12 3l2.6 5.4 5.9.8-4.3 4.1 1 5.8L12 16.3 6.8 19l1-5.8L3.5 9.2l5.9-.8z" fill="none" stroke="#fff" stroke-width="1.6"/></svg></div>
    <h3>Risk Assessment</h3>
    <p>Lorem ipsum dolor sit amet, conse or incididunt ut labore et .</p>
  </div>
  <div class="card" style="left:436px">
    <div class="img" role="img" aria-label="Laptop with floating digital interface panels" style="background:linear-gradient(135deg,#56698a,#a9b6ca)"></div>
    <div class="ic"><svg width="24" height="24" viewBox="0 0 24 24"><circle cx="12" cy="12" r="8" fill="none" stroke="#fff" stroke-width="1.6"/><path d="M9 12l2 2 4-4" fill="none" stroke="#fff" stroke-width="1.6"/></svg></div>
    <h3>Safety Audits</h3>
    <p>Lorem ipsum dolor sit amet, conse or incididunt ut labore et .</p>
  </div>
  <div class="card" style="left:790px">
    <div class="img" role="img" aria-label="Colleagues reviewing documents at a table" style="background:linear-gradient(135deg,#8c8f99,#d4d3d0)"></div>
    <div class="ic"><svg width="24" height="24" viewBox="0 0 24 24"><circle cx="12" cy="12" r="8" fill="none" stroke="#fff" stroke-width="1.6"/><circle cx="9" cy="10" r="1" fill="#fff"/><circle cx="15" cy="10" r="1" fill="#fff"/><path d="M8.5 15.5h7" stroke="#fff" stroke-width="1.6"/></svg></div>
    <h3>Incident Investigation</h3>
    <p>Lorem ipsum dolor sit amet, conse or incididunt ut labore et .</p>
  </div>
</section>

<!-- Why choose us -->
<section>
  <div class="abs why-bg"></div>
  <div class="eyebrow" style="left:527px;top:2030px;padding-bottom:3px;border-bottom-width:1px">WHY CHOOSE US</div>
  <h2 class="h2" style="left:0;width:1167px;text-align:center;top:2066px;font-size:42px">Why Choose Us</h2>
  <div class="abs why-halo"></div>
  <div class="abs why-ring"></div>
  <div class="abs why-photo" role="img" aria-label="Smiling professional with arms crossed"></div>

  <div class="feat" style="left:79px;top:2184px;width:321px"><h4 style="left:48px">Client-centric</h4><p style="left:48px">Lorem ipsum dolor sit amet, consectetur adipiscing</p></div>
  <div class="feat" style="left:82px;top:2329px;width:293px"><h4 style="left:50px">Cost-Effective</h4><p style="left:50px">Lorem ipsum dolor sit amet, consectetur adipiscing</p></div>
  <div class="feat" style="left:79px;top:2481px;width:321px"><h4 style="left:48px">Professional</h4><p style="left:48px">Lorem ipsum dolor sit amet, consectetur adipiscing</p></div>
  <div class="feat" style="left:797px;top:2184px;width:319px"><h4 style="left:46px">Proven Track Record</h4><p style="left:46px">Lorem ipsum dolor sit amet, consectetur adipiscing</p></div>
  <div class="feat" style="left:820px;top:2329px;width:294px"><h4 style="left:48px">Confidentiality</h4><p style="left:48px">Lorem ipsum dolor sit amet, consectetur adipiscing</p></div>
  <div class="feat" style="left:797px;top:2481px;width:319px"><h4 style="left:48px">Regulatory Compliance</h4><p style="left:48px">Lorem ipsum dolor sit amet, consectetur adipiscing</p></div>

  <div class="bub" style="left:374px;top:2203px"><svg width="28" height="28" viewBox="0 0 28 28"><circle cx="14" cy="10" r="5" fill="none" stroke="var(--blue)" stroke-width="1.6"/><path d="M5 23c1-5 5-7 9-7s8 2 9 7z" fill="none" stroke="var(--blue)" stroke-width="1.6"/></svg></div>
  <div class="bub" style="left:350px;top:2348px"><svg width="28" height="28" viewBox="0 0 28 28"><path d="M9 15V8a1.5 1.5 0 0 1 3 0v5V6a1.5 1.5 0 0 1 3 0v7V7a1.5 1.5 0 0 1 3 0v8l1-3a1.5 1.5 0 0 1 3 1l-2 7c-1 3-3 4-6 4h-2c-3 0-5-2-5-5z" fill="none" stroke="var(--blue)" stroke-width="1.5"/></svg></div>
  <div class="bub" style="left:374px;top:2500px"><svg width="28" height="28" viewBox="0 0 28 28"><path d="M6 14a8 8 0 0 1 14-5M22 14a8 8 0 0 1-14 5" fill="none" stroke="var(--blue)" stroke-width="1.6"/><path d="M20 4v5h-5M8 24v-5h5" fill="none" stroke="var(--blue)" stroke-width="1.6"/><circle cx="14" cy="14" r="3" fill="none" stroke="var(--blue)" stroke-width="1.6"/></svg></div>
  <div class="bub" style="left:754px;top:2203px"><svg width="28" height="28" viewBox="0 0 28 28"><path d="M14 4l3 6 6.5 1-4.7 4.5 1.1 6.5L14 19l-5.9 3 1.1-6.5L4.5 11l6.5-1z" fill="none" stroke="var(--blue)" stroke-width="1.6"/></svg></div>
  <div class="bub" style="left:780px;top:2348px"><svg width="28" height="28" viewBox="0 0 28 28"><circle cx="12" cy="8" r="4" fill="none" stroke="var(--blue)" stroke-width="1.6"/><path d="M4 23c1-5 4-7 8-7M15 22l8-8 2 2-8 8h-2z" fill="none" stroke="var(--blue)" stroke-width="1.6"/></svg></div>
  <div class="bub" style="left:754px;top:2500px"><svg width="28" height="28" viewBox="0 0 28 28"><circle cx="14" cy="14" r="4" fill="none" stroke="var(--blue)" stroke-width="1.6"/><path d="M14 4v3M14 21v3M4 14h3M21 14h3M7 7l2 2M19 19l2 2M7 21l2-2M19 9l2-2" stroke="var(--blue)" stroke-width="1.6"/><circle cx="14" cy="14" r="7.5" fill="none" stroke="var(--blue)" stroke-width="1.6"/></svg></div>
</section>

<!-- Contact -->
<section>
  <div class="abs contact-band" role="img" aria-label="Person at a laptop with digital document icons overlaid">
    <h2>CONTACT US</h2>
    <div class="sub">Fill out the form below to get connected with us.</div>
  </div>
  <div class="citem" style="top:2826px">
    <div class="cc"><svg width="22" height="22" viewBox="0 0 24 24"><path d="M5 3h4l2 5-2.5 1.5a11 11 0 0 0 6 6L16 13l5 2v4a2 2 0 0 1-2 2A16 16 0 0 1 3 5a2 2 0 0 1 2-2z" fill="none" stroke="var(--blue)" stroke-width="1.6"/></svg></div>
    <div><small>Our Phone Number:</small><b style="font-size:24px;line-height:28px">555 014 2290</b></div>
  </div>
  <div class="citem" style="top:2888px">
    <div class="cc"><svg width="22" height="22" viewBox="0 0 24 24"><path d="M12 2a7 7 0 0 0-7 7c0 5 7 13 7 13s7-8 7-13a7 7 0 0 0-7-7z" fill="none" stroke="var(--blue)" stroke-width="1.6"/><circle cx="12" cy="9" r="2.5" fill="none" stroke="var(--blue)" stroke-width="1.6"/></svg></div>
    <div><small>Our Location:</small><b style="width:300px">48 Orchard Lane, Brookfield 20415</b></div>
  </div>
  <div class="citem" style="top:2968px">
    <div class="cc"><svg width="22" height="22" viewBox="0 0 24 24"><rect x="3" y="6" width="18" height="13" rx="1" fill="none" stroke="var(--blue)" stroke-width="1.6"/><path d="M3 7l9 7 9-7" fill="none" stroke="var(--blue)" stroke-width="1.6"/></svg></div>
    <div><small>Our Email Address:</small><b>info@lumengrove.example</b></div>
  </div>
  <form class="abs form">
    <div class="field" style="top:23px">Full Name</div>
    <div class="field" style="top:71px">Email Address</div>
    <div class="field" style="top:119px">Phone Number</div>
    <div class="field" style="top:167px;height:112px">Message</div>
    <div class="submit">SUBMIT</div>
  </form>
</section>

<!-- Testimonials -->
<section>
  <div class="eyebrow" style="left:540px;top:3218px;padding-bottom:3px;border-bottom-width:1px">TESTIMONIALS</div>
  <h2 class="h2" style="left:0;width:1180px;text-align:center;top:3254px;font-size:42px">What our clients are saying</h2>
  <div class="tcard" style="left:90px">
    <div class="bar"></div><div class="q"></div>
    <div class="stars">★★★★★</div>
    <p>Lorem ipsum dolor sit amet, consectetur adipiscing elit, sed do eiusmod tempor incididunt ut labore et dolore magna aliqua. Ut enim</p>
    <h5>Mara Ellison</h5><span class="loc">Elm Ridge</span>
    <div class="av" role="img" aria-label="Client portrait"></div>
  </div>
  <div class="tcard" style="left:612px">
    <div class="bar"></div><div class="q"></div>
    <div class="stars">★★★★★</div>
    <p>Lorem ipsum dolor sit amet, consectetur adipiscing elit, sed do eiusmod tempor incididunt ut labore et dolore magna aliqua. Ut enim</p>
    <h5>Mara Ellison</h5><span class="loc">Elm Ridge</span>
    <div class="av" role="img" aria-label="Client portrait" style="background:linear-gradient(135deg,#e6d6c0,#5b5046)"></div>
  </div>
  <div class="abs dots"><i></i><i></i><i class="on"></i><i></i></div>
</section>

<!-- Footer -->
<svg class="abs" style="left:0;top:3660px" width="1200" height="100" viewBox="0 0 1200 100">
  <path d="M0 60C250 10 450 10 700 40S1000 50 1200 20V100H0Z" fill="var(--sky)"/>
  <path d="M0 72C250 30 450 30 700 55S1000 60 1200 40V100H0Z" fill="var(--footer)"/>
</svg>
<footer class="abs footer">
  <div class="abs" style="left:165px;top:140px;display:flex;align-items:center;gap:8px;color:#fff;font-weight:700;font-size:18px"><i style="width:16px;height:16px;border-radius:50%;background:#fff;display:block"></i>Lumen Grove</div>
  <p class="abs" style="left:126px;top:193px;width:300px;font-size:12px;line-height:21px">Lorem ipsum dolor sit amet, consectetur adipiscing elit, sed do eiusmod tempor incididunt ut</p>
  <i class="soc on" style="left:127px"></i><i class="soc" style="left:167px"></i><i class="soc" style="left:207px"></i><i class="soc" style="left:247px"></i>

  <h6 style="left:489px">Quick Links</h6>
  <div class="flinks" style="left:489px">Home<br>How it works<br>Products<br>Pricing<br>About Us<br>Contact Us</div>
  <div class="flinks" style="left:625px">Cookies Policy<br>Terms of Use<br>Careers<br>Our Team<br>More</div>

  <h6 style="left:826px">Newsletters</h6>
  <p class="abs" style="left:826px;top:162px;width:250px;font-size:11.5px;line-height:21px">Lorem ipsum dolor sit amet, consectetur adi piscing elit, sed do eiusmod tempor</p>
  <div class="news">Enter Email Address</div>
  <div class="news-btn"><svg width="12" height="18" viewBox="0 0 12 18"><path d="M2 2l7 7-7 7" fill="none" stroke="#fff" stroke-width="2.4"/></svg></div>

  <div class="finfo" style="left:125px">
    <div class="fc"><svg width="18" height="18" viewBox="0 0 24 24"><path d="M12 2a7 7 0 0 0-7 7c0 5 7 13 7 13s7-8 7-13a7 7 0 0 0-7-7z" fill="#dce8fa"/></svg></div>
    <div><b>Address</b><small>48 Orchard Lane</small></div>
  </div>
  <div class="finfo" style="left:365px">
    <div class="fc on"><svg width="18" height="18" viewBox="0 0 24 24"><rect x="3" y="6" width="18" height="13" fill="none" stroke="#fff" stroke-width="1.8"/><path d="M3 7l9 7 9-7" fill="none" stroke="#fff" stroke-width="1.8"/></svg></div>
    <div><b>Email Us</b><small>support@lumengrove.example</small></div>
  </div>
  <div class="finfo" style="left:632px">
    <div class="fc"><svg width="18" height="18" viewBox="0 0 24 24"><path d="M5 3h4l2 5-2.5 1.5a11 11 0 0 0 6 6L16 13l5 2v4a2 2 0 0 1-2 2A16 16 0 0 1 3 5a2 2 0 0 1 2-2z" fill="#dce8fa"/></svg></div>
    <div><b>Contact Us</b><small>+1 (555) 014 2290</small></div>
  </div>
  <div class="finfo" style="left:859px">
    <div class="fc"><svg width="20" height="20" viewBox="0 0 24 24"><circle cx="12" cy="12" r="9" fill="none" stroke="#dce8fa" stroke-width="1.8"/><path d="M12 7v5l3 2" fill="none" stroke="#dce8fa" stroke-width="1.8"/></svg></div>
    <div><b>Opening Hour</b><small>Mon - Friday 10 am - 8pm</small></div>
  </div>
  <div class="abs" style="left:125px;top:489px;width:948px;height:1px;background:#4a82d4"></div>
  <div class="abs" style="left:0;width:1188px;text-align:center;top:507px;font-size:12px;color:#fff">Lumen Grove</div>
</footer>

</body>
</html>
```